Elegant wordpress web page for wedding rental of hand sanitizers

We want to rent our hand sanitizing towers out for high-end weddings. We need a very elegant, sophisticated page that describes our offering. You can see an ugly first draft here: trelvo.com/weddings
Target Market(s)
Wedding planners, wedding parents
Number of Pages Required
1 page
Font styles to use
Serif
Script
Colors
Designer to choose colors to be used in the design.
Requirements
Nice to have
- Two wedding-related sites for inspiration: quietorchardweddings-dot-com and fernlaneservices-dot-com

```html
<!DOCTYPE html>
<html lang="en">
<head>
<meta charset="utf-8">
<title>Trelvo — Wedding Sanitizer Rental</title>
<link href="https://fonts.googleapis.com/css2?family=Poppins:wght@400;500;600;700&family=Playball&display=swap" rel="stylesheet">
<style>
:root{
  --blue:#1a9ad6;
  --blue-dark:#0f7fbf;
  --blue-light:#4bb3e6;
  --navy:#1b1f33;
  --ink:#222;
  --text:#666;
  --soft:#f3f4f6;
  --white:#fff;
}
*{margin:0;padding:0;box-sizing:border-box}
html,body{width:1200px;height:4835px;overflow:hidden}
body{position:relative;font-family:'Poppins',sans-serif;color:var(--text);background:var(--white)}
.abs{position:absolute}
.script{font-family:'Playball',cursive;color:var(--ink);font-weight:400}
.pill{position:absolute;display:flex;align-items:center;justify-content:center;border-radius:30px;font-size:13px;font-weight:600;letter-spacing:.3px}
.pill-outline{background:var(--white);color:var(--blue);box-shadow:0 4px 14px rgba(26,154,214,.22);border:1px solid #e3f1f9}
.pill-solid{background:var(--blue);color:var(--white)}
.photo{position:absolute}
.drop{position:absolute}
/* header */
.site-header{position:absolute;left:0;top:0;width:1200px;height:83px;background:var(--white);z-index:3}
.brand{position:absolute;left:150px;top:18px;font-size:34px;font-weight:600;color:var(--blue);letter-spacing:-.5px}
.nav{position:absolute;left:400px;top:42px;display:flex;gap:26px;font-size:12.5px;font-weight:600;color:var(--ink)}
.nav .active{color:var(--blue)}
.quote-btn{position:absolute;left:902px;top:0;width:148px;height:100px;background:var(--blue);color:var(--white);font-size:15px;font-weight:600;display:flex;align-items:center;justify-content:center;padding-bottom:18px;z-index:4}
/* hero */
.hero{position:absolute;left:0;top:83px;width:1200px;height:524px;background:linear-gradient(120deg,#4a3b2f 0%,#6b5848 40%,#8c7a66 65%,#5a4a3c 100%)}
.hero-lead{position:absolute;left:150px;top:124px;font-size:25px;color:var(--white)}
.hero-title{position:absolute;left:150px;top:165px;font-size:56px;line-height:58px;color:var(--white)}
.hero-arrow{position:absolute;top:232px;width:38px;height:38px;border-radius:50%;background:rgba(0,0,0,.35);color:#fff;display:flex;align-items:center;justify-content:center;font-size:16px}
.dots{position:absolute;top:442px;left:555px;display:flex;gap:6px}
.dots span{width:12px;height:12px;border-radius:50%;border:2px solid #fff}
.dots .on{background:var(--blue);border-color:var(--blue)}
/* services */
.services{position:absolute;left:0;top:607px;width:1200px;height:501px;background:var(--soft)}
.service{position:absolute;width:280px;text-align:center;top:0}
.service h3{font-family:'Playball',cursive;font-weight:400;font-size:44px;color:var(--ink);margin-top:160px;line-height:44px}
.service .sub{color:var(--blue);font-size:17px;margin-top:-4px}
.service p{font-size:13.5px;line-height:26px;margin-top:20px}
.feature-card{position:absolute;left:447px;top:575px;width:306px;height:533px;background:var(--white);z-index:2}
.feature-card .banner{position:absolute;left:0;bottom:0;width:306px;height:48px;background:var(--blue);color:#fff;font-weight:600;font-size:20px;display:flex;align-items:center;justify-content:center}
/* why */
.section-title{position:absolute;left:0;width:1200px;text-align:center;font-size:46px}
.section-sub{position:absolute;left:0;width:1200px;text-align:center;font-size:13.5px;line-height:25px}
.list-item{position:absolute;left:686px;width:380px;font-size:14.5px;line-height:27px;color:#555}
/* customize */
.cust-card{position:absolute;top:1987px;width:282px;height:376px;background:var(--white);box-shadow:0 4px 18px rgba(0,0,0,.08);text-align:center}
.cust-card h4{position:absolute;top:248px;width:100%;font-size:16.5px;font-weight:600;color:var(--ink)}
.cust-card p{position:absolute;top:282px;left:25px;width:232px;font-size:14px;line-height:26px}
/* offers */
.offer{position:absolute;left:623px;width:440px;height:132px}
.offer .thumb{position:absolute;left:15px;top:16px;width:100px;height:100px;border-radius:50%}
.offer .from{position:absolute;left:135px;top:20px;font-size:12px;color:#888}
.offer .from b{color:var(--blue);font-weight:500}
.offer h5{position:absolute;left:135px;top:40px;font-size:18.5px;font-weight:500;color:var(--ink)}
.offer p{position:absolute;left:135px;top:76px;font-size:12.5px;line-height:21px;color:#888;width:290px}
/* review */
.review{position:absolute;left:0;top:3225px;width:1200px;height:512px;background:linear-gradient(90deg,#2a2a30 0%,#3b3430 45%,#6a5038 70%,#3a2f29 100%)}
.review-box{position:absolute;left:150px;top:3480px;width:545px;height:346px;background:linear-gradient(135deg,#28a6e0,#1587c4);border-radius:0 0 60px 0;color:#fff;text-align:center}
/* footer */
.footer{position:absolute;left:0;top:4545px;width:1200px;height:290px;background:var(--navy);color:#fff}
.footer h6{position:absolute;top:76px;font-size:17px;font-weight:500;letter-spacing:.3px}
.footer .line{position:absolute;font-size:14px;display:flex;align-items:center;gap:12px}
.social{position:absolute;top:112px;left:481px;display:flex;gap:10px}
.social span{width:38px;height:38px;border-radius:50%;border:1.5px solid #fff}
</style>
</head>
<body>

<header class="site-header">
  <div class="brand">trelvo</div>
  <nav class="nav">
    <span class="active">HOME</span><span>ABOUT</span><span>PRODUCTS</span><span>INDUSTRY SOLUTIONS</span><span>CONTACT</span>
  </nav>
</header>
<div class="quote-btn">GET A QUOTE</div>

<section class="hero" role="img" aria-label="Wedding venue with draped ceremony arch, chairs and a photo sanitizer stand">
  <div class="hero-lead">Customize Your Sanitizer With</div>
  <div class="hero-title script" style="color:#fff">Any Photo, Any Size &amp;<br>Any Shape</div>
  <div class="pill pill-solid" style="left:150px;top:320px;width:150px;height:42px">RENT NOW</div>
  <div class="pill" style="left:318px;top:320px;width:152px;height:42px;border:2px solid #fff;color:#fff">READ MORE</div>
  <div class="hero-arrow" style="left:64px">&#8249;</div>
  <div class="hero-arrow" style="left:1098px">&#8250;</div>
  <div class="dots"><span></span><span></span><span class="on"></span><span></span><span></span></div>
</section>

<section class="services">
  <svg class="abs" style="left:0;bottom:0" width="1200" height="60" viewBox="0 0 1200 60"><path d="M0 40 C200 10 400 60 600 35 S1000 10 1200 38 V60 H0Z" fill="#fff"/></svg>
  <div class="service" style="left:140px">
    <svg class="drop" style="left:100px;top:58px" width="80" height="100" viewBox="0 0 80 100"><path d="M40 2 C40 2 4 46 4 64 a36 36 0 0 0 72 0 C76 46 40 2 40 2Z" fill="var(--blue)"/><circle cx="34" cy="66" r="11" fill="none" stroke="#fff" stroke-width="4"/><circle cx="46" cy="66" r="11" fill="none" stroke="#fff" stroke-width="4"/></svg>
    <h3>Wedding</h3><div class="sub">Rental</div>
    <p>Lorem ipsum dolor sit amet, adipiscing elit. Proin tempor justo sed quam luctu nec semper lectus iaculis.</p>
  </div>
  <div class="pill pill-outline" style="left:205px;top:365px;width:150px;height:44px">GET A QUOTE</div>
  <div class="service" style="left:780px">
    <svg class="drop" style="left:100px;top:58px" width="80" height="100" viewBox="0 0 80 100"><path d="M40 2 C40 2 4 46 4 64 a36 36 0 0 0 72 0 C76 46 40 2 40 2Z" fill="var(--blue)"/><circle cx="33" cy="52" r="5" fill="#fff"/><circle cx="48" cy="52" r="5" fill="#fff"/><path d="M27 84 L30 60 H37 L39 84Z M42 84 L44 60 H52 L56 84Z" fill="#fff"/></svg>
    <h3>Reception</h3><div class="sub">Rental</div>
    <p>Lorem ipsum dolor sit amet, adipiscing elit. Proin tempor justo sed quam luctu nec semper lectus iaculis.</p>
  </div>
  <div class="pill pill-outline" style="left:845px;top:365px;width:150px;height:44px">GET A QUOTE</div>
</section>

<div class="feature-card">
  <div class="photo" role="img" aria-label="White sanitizer stand topped with a dancing couple photo" style="left:43px;top:40px;width:220px;height:420px;background:linear-gradient(180deg,#3a3a48 0%,#5a4a55 25%,#e8e9ec 30%,#f5f6f8 100%);border-radius:10px"></div>
  <div class="banner">WELCOME YOUR GUESTS!</div>
</div>

<h2 class="section-title script" style="top:1180px">Why we are Unique and Different?</h2>
<p class="section-sub" style="top:1258px">Why have a generic, industrial hand sanitizer when you could have<br>something truly unique and different?</p>

<svg class="abs" style="left:110px;top:1360px" width="460" height="345" viewBox="0 0 460 345"><path d="M72 3 H448 V280 A60 60 0 0 1 388 340 H3 V72 A69 69 0 0 1 72 3Z" fill="none" stroke="var(--blue)" stroke-width="3"/></svg>
<div class="photo" role="img" aria-label="Couple photo sanitizer stand beside a bridal bouquet" style="left:150px;top:1326px;width:408px;height:342px;border-radius:60px 0 60px 0;background:linear-gradient(135deg,#6b5a4e,#a89686 50%,#d8d2cc)"></div>

<svg class="drop" style="left:617px;top:1346px" width="40" height="54" viewBox="0 0 40 54"><path d="M20 1 C20 1 2 24 2 34 a18 18 0 0 0 36 0 C38 24 20 1 20 1Z" fill="var(--blue)"/><rect x="12" y="27" width="16" height="14" fill="none" stroke="#fff" stroke-width="2"/></svg>
<div class="list-item" style="top:1350px">Customize the photo above the spout and the spout decoration</div>
<svg class="drop" style="left:617px;top:1438px" width="40" height="54" viewBox="0 0 40 54"><path d="M20 1 C20 1 2 24 2 34 a18 18 0 0 0 36 0 C38 24 20 1 20 1Z" fill="var(--blue)"/><path d="M12 42 L28 26 M12 26 L28 42" stroke="#fff" stroke-width="3"/></svg>
<div class="list-item" style="top:1453px">Choose any size and shape photo you wish</div>
<svg class="drop" style="left:617px;top:1520px" width="40" height="54" viewBox="0 0 40 54"><path d="M20 1 C20 1 2 24 2 34 a18 18 0 0 0 36 0 C38 24 20 1 20 1Z" fill="var(--blue)"/><rect x="15" y="24" width="10" height="18" rx="2" fill="none" stroke="#fff" stroke-width="2"/></svg>
<div class="list-item" style="top:1513px">Choose from our standard spout decorations or design one of your own.&nbsp; We'll take care of producing and fitting it.</div>
<div class="pill pill-outline" style="left:617px;top:1630px;width:290px;height:45px">CHECK PRICE AND AVAILABILITY</div>

<svg class="abs" style="left:0;top:1777px" width="1200" height="430" viewBox="0 0 1200 430">
  <defs><linearGradient id="band" x1="0" x2="1"><stop offset="0" stop-color="#3aa8de"/><stop offset="1" stop-color="#2e9fd8"/></linearGradient></defs>
  <path d="M0 0 H1200 V405 C900 240 300 240 0 405Z" fill="url(#band)"/>
</svg>
<h2 class="section-title script" style="top:1850px;color:#fff;font-size:42px">Customize Your Sanitizer</h2>
<p class="section-sub" style="top:1912px;color:#fff;font-size:14px">With Any Photo, Any Size, Any Shape</p>

<div class="cust-card" style="left:150px">
  <div class="photo" role="img" aria-label="Hands holding printed wedding photos" style="left:0;top:0;width:282px;height:184px;background:linear-gradient(135deg,#7a6a60,#d9d2cc)"></div>
  <svg class="drop" style="left:107px;top:128px" width="68" height="92" viewBox="0 0 68 92"><path d="M34 2 C34 2 3 42 3 58 a31 31 0 0 0 62 0 C65 42 34 2 34 2Z" fill="var(--blue)"/><rect x="20" y="48" width="28" height="20" rx="2" fill="none" stroke="#fff" stroke-width="3"/></svg>
  <h4>CHOOSE A PHOTO</h4><p>Choose a photo of the happy couple, the proud parents, or anything else you wish</p>
</div>
<div class="cust-card" style="left:462px">
  <div class="photo" role="img" aria-label="Design desk with a monitor and colour swatches" style="left:0;top:0;width:282px;height:184px;background:linear-gradient(135deg,#bcc3c9,#eceff1)"></div>
  <svg class="drop" style="left:107px;top:128px" width="68" height="92" viewBox="0 0 68 92"><path d="M34 2 C34 2 3 42 3 58 a31 31 0 0 0 62 0 C65 42 34 2 34 2Z" fill="var(--blue)"/><path d="M20 72 L48 44 M20 44 L48 72" stroke="#fff" stroke-width="4"/></svg>
  <h4>CHOOSE A SIZE</h4><p>Choose any size or shape you wish, up to 24x36"</p>
</div>
<div class="cust-card" style="left:770px">
  <div class="photo" role="img" aria-label="Wedding aisle lined with floral arrangements" style="left:0;top:0;width:282px;height:184px;background:linear-gradient(135deg,#8a7a5e,#d8c9b2)"></div>
  <svg class="drop" style="left:107px;top:128px" width="68" height="92" viewBox="0 0 68 92"><path d="M34 2 C34 2 3 42 3 58 a31 31 0 0 0 62 0 C65 42 34 2 34 2Z" fill="var(--blue)"/><rect x="19" y="46" width="12" height="12" fill="#fff"/><circle cx="43" cy="52" r="7" fill="#fff"/><circle cx="25" cy="70" r="6" fill="#fff"/><path d="M43 62 L50 76 H36Z" fill="#fff"/></svg>
  <h4>CHOOSE A SHAPE</h4><p>We take care of all production and customization</p>
</div>
<div class="pill pill-outline" style="left:455px;top:2408px;width:290px;height:46px">CHECK PRICE AND RENT NOW</div>

<div class="photo" role="img" aria-label="Bride and groom under sparklers at night" style="left:116px;top:2554px;width:212px;height:211px;background:linear-gradient(160deg,#2a2c38,#7d7a80)"></div>
<div class="photo" role="img" aria-label="Sanitizer stands with gold vases of roses" style="left:224px;top:2633px;width:326px;height:387px;background:linear-gradient(160deg,#e4e0e6,#c9bcb0)"></div>
<div class="photo" role="img" aria-label="Hands being washed with soap" style="left:116px;top:2910px;width:292px;height:230px;background:linear-gradient(160deg,#cfd6dc,#b59a8a)"></div>

<div class="abs" style="left:623px;top:2580px;font-size:14px;font-weight:500;color:var(--blue)">Our Hand Sanitizer</div>
<h2 class="abs script" style="left:623px;top:2604px;font-size:44px">Our Special Offers</h2>

<div class="offer" style="top:2700px">
  <div class="thumb" role="img" aria-label="Marriage package sanitizer" style="background:linear-gradient(135deg,#6b5a52,#d2c8c0)"></div>
  <div class="from">Start From: <b>$ 25.00</b></div><h5>Marriage Package</h5>
  <p>Lorem ipsum dolor sit amet, consectetur adipiscing sed do eiusmod tempor</p>
</div>
<div class="offer" style="top:2845px;background:#fff;border-radius:70px;box-shadow:0 6px 24px rgba(0,0,0,.1)">
  <div class="thumb" role="img" aria-label="Flower vase package sanitizer" style="background:linear-gradient(135deg,#5d6a50,#d8cfc2)"></div>
  <div class="from">Start From: <b>$ 35.00</b></div><h5>Flower Vase Package</h5>
  <p>Lorem ipsum dolor sit amet, consectetur adipiscing sed do eiusmod tempor</p>
</div>
<div class="offer" style="top:2995px">
  <div class="thumb" role="img" aria-label="Wedding cake package sanitizer" style="background:linear-gradient(135deg,#6a5b55,#e0d8d2)"></div>
  <div class="from">Start From: <b>$ 50.0</b></div><h5>Wedding Cake Package</h5>
  <p>Lorem ipsum dolor sit amet, consectetur adipiscing sed do eiusmod tempor</p>
</div>

<section class="review" role="img" aria-label="Couple dancing under string lights beside a photo sanitizer stand">
  <div class="abs" style="left:150px;top:90px;font-size:14px;font-weight:500;color:#fff">Our Hand Sanitizer</div>
  <div class="abs script" style="left:150px;top:112px;font-size:42px;line-height:56px;color:#fff">Our Happy Customer<br>Review</div>
  <div class="hero-arrow" style="left:612px;top:186px;background:rgba(255,255,255,.15);width:34px;height:34px">&#8592;</div>
  <div class="hero-arrow" style="left:660px;top:186px;background:rgba(255,255,255,.15);width:34px;height:34px">&#8594;</div>
</section>
<div class="review-box">
  <p class="abs" style="left:35px;top:38px;width:475px;font-size:14px;line-height:30px">Aliquam tincidunt sapien et nisi felacinia ante andeiyfringilla. Nullam vestibulum venenatis ante etporttiteoy into onusce sit ametbib enduerat. Cras vestibulu venenatis ante etporttiteoy into onusce sit ametbib enduerat. Cras commodo niduitings felacinia ante andeiyfringilla. Nullam vestibulum venenatis ante etporttiteoy into onusce.</p>
  <div class="abs" role="img" aria-label="Reviewer portrait" style="left:130px;top:268px;width:60px;height:60px;border-radius:50%;background:#e8eef2;border:3px solid #fff"></div>
  <div class="abs" style="left:210px;top:268px;font-size:18px;font-weight:500">John Doe</div>
  <div class="abs" style="left:215px;top:300px;font-size:14px">CEO, Creative Agency pvt.</div>
</div>

<div class="photo" role="img" aria-label="Three white sanitizer stands with hexagon, rectangle and round couple photos" style="left:50px;top:3900px;width:510px;height:470px;background:linear-gradient(180deg,#8a7a72 0%,#c8c0ba 25%,#f1f2f4 40%,#ffffff 100%)"></div>
<h2 class="abs script" style="left:605px;top:3910px;font-size:42px;line-height:52px">Greet Your Guests With An<br>Act Of Care</h2>
<svg class="drop" style="left:605px;top:4030px" width="40" height="54" viewBox="0 0 40 54"><path d="M20 1 C20 1 2 24 2 34 a18 18 0 0 0 36 0 C38 24 20 1 20 1Z" fill="var(--blue)"/><circle cx="20" cy="34" r="7" fill="#fff"/></svg>
<div class="list-item" style="left:668px;top:4034px;font-size:14px">Make your friends and family feel welcome and safe with a rugged, durable hand sanitizer from Trelvo</div>
<svg class="drop" style="left:605px;top:4118px" width="40" height="54" viewBox="0 0 40 54"><path d="M20 1 C20 1 2 24 2 34 a18 18 0 0 0 36 0 C38 24 20 1 20 1Z" fill="var(--blue)"/><path d="M12 36 L20 28 L28 36" stroke="#fff" stroke-width="3" fill="none"/></svg>
<div class="list-item" style="left:668px;top:4120px;font-size:14px">Our battery-powered dispensers are reliable, wireless, and touchless</div>
<svg class="drop" style="left:605px;top:4204px" width="40" height="54" viewBox="0 0 40 54"><path d="M20 1 C20 1 2 24 2 34 a18 18 0 0 0 36 0 C38 24 20 1 20 1Z" fill="var(--blue)"/><rect x="13" y="24" width="14" height="18" fill="none" stroke="#fff" stroke-width="2"/></svg>
<div class="list-item" style="left:668px;top:4206px;font-size:14px">Filled with your choice from our wide range of sanitizing products</div>
<div class="pill pill-outline" style="left:605px;top:4310px;width:290px;height:46px">CHECK PRICE AND RENT NOW</div>

<svg class="abs" style="left:0;top:4430px" width="1200" height="120" viewBox="0 0 1200 120">
  <defs><linearGradient id="arc" x1="0" x2="1"><stop offset="0" stop-color="#1587c4"/><stop offset=".5" stop-color="#3fb4ea"/><stop offset="1" stop-color="#1587c4"/></linearGradient></defs>
  <path d="M110 118 C350 -10 850 -10 1090 118 C850 30 350 30 110 118Z" fill="url(#arc)"/>
  <path d="M0 116 C300 30 900 30 1200 116 V120 H0Z" fill="var(--navy)"/>
  <path d="M80 120 C330 20 870 20 1120 120Z" fill="var(--navy)"/>
</svg>
<footer class="footer">
  <div class="abs" style="left:0;top:-5px;width:1200px;text-align:center;font-size:36px;font-weight:600;color:var(--blue)">trelvo</div>
  <h6 style="left:160px">CONTACT US</h6>
  <div class="line" style="left:160px;top:117px"><svg width="14" height="14" viewBox="0 0 24 24"><path d="M6 2 L10 6 L7.5 9 C9 12 12 15 15 16.5 L18 14 L22 18 L19 22 C10 21 3 14 2 5Z" fill="#fff"/></svg>(+1) 123 456 7890</div>
  <div class="line" style="left:160px;top:160px"><svg width="12" height="16" viewBox="0 0 12 16"><path d="M6 0 a6 6 0 0 1 6 6 C12 10 6 16 6 16 S0 10 0 6 A6 6 0 0 1 6 0Z" fill="#fff"/><circle cx="6" cy="6" r="2.2" fill="var(--navy)"/></svg>123 sample city, Wood, USA</div>
  <h6 style="left:481px">FOLLOW US</h6>
  <div class="social"><span></span><span></span><span></span><span></span></div>
  <h6 style="left:780px">NEWSLETTER SUBSCRIBE</h6>
  <div class="abs" style="left:780px;top:113px;width:260px;height:36px;border:1px solid #fff;font-size:12px;padding:9px 10px">Enter Email</div>
  <div class="pill pill-solid" style="left:780px;top:159px;width:108px;height:34px;font-size:11.5px">SUBSCRIBE</div>
  <div class="abs" style="left:0;top:250px;width:1200px;text-align:center;font-size:13px">Copyrights © 2021 Trelvo.&nbsp; All Rights Reserved&nbsp;&nbsp;|&nbsp;&nbsp;Site Map&nbsp;&nbsp;|&nbsp;&nbsp;Privacy Policy.</div>
</footer>

</body>
</html>
```